Design of an attractive membership brochure/membership card for an Electrical Business

Hi, we are an electrical business based in Sydney, Australia.

Our design's aim is to attract and target new customers into using our business as a repeat for anything electrical in their home. We would be handing this out to them after a job is completed and they're happy with the service.
We're thinking of a brochure, possibly additional membership cards with personalized number ID's for each client.

Open to ideas, but some of the things we want to include on our brochure are perks of why the client should sign up with us as a lifetime client
- Discounted emergency call out fees outside of normal hours
- Lifetime membership price, one time payment
- Exclusive 10% member discount on all future jobs
- Priority on any during business hour jobs or emergencies

If any other questions please don't hesitate to reach out.
We've attached our logo for reference for the mock designs.
Our website
https://brightwirecrew.com.au/

```html
<!DOCTYPE html>
<html lang="en">
<head>
<meta charset="utf-8">
<title>Bright Wire Crew – Membership Brochure</title>
<link href="https://fonts.googleapis.com/css2?family=Montserrat:wght@400;500;600;700;800;900&display=swap" rel="stylesheet">
<style>
:root{
  --red:#e21f26;
  --red-dark:#b5161c;
  --black:#0c0c0c;
  --white:#ffffff;
  --grey:#d6d6d6;
  --text-dark:#1a1a1a;
}
*{box-sizing:border-box;margin:0;padding:0}
html,body{width:803px;height:1200px;overflow:hidden}
body{background:var(--grey);font-family:'Montserrat',Arial,sans-serif;position:relative}
.spread{position:absolute;left:21px;width:761px;height:530px;background:var(--white);overflow:hidden;box-shadow:0 4px 14px rgba(0,0,0,.25)}
.spread--outside{top:55px}
.spread--inside{top:615px}
.panel{position:absolute;top:0;width:381px;height:530px;overflow:hidden}
.panel--left{left:0}
.panel--right{left:380px}
.shapes{position:absolute;inset:0;width:100%;height:100%}
.photo{position:absolute}
.photo--bath{left:0;top:0;width:190px;height:140px;background:linear-gradient(135deg,#f2efe9,#cdbfa8 70%,#a88a62)}
.photo--kitchen{left:196px;top:0;width:185px;height:140px;background:linear-gradient(160deg,#fbfaf7,#d9d2c6 60%,#6e5a44)}
.photo--lounge{left:60px;top:146px;width:321px;height:124px;background:linear-gradient(120deg,#eae6df,#c8b59b 55%,#8a6b4b);clip-path:polygon(0 0,100% 0,100% 100%,18% 100%)}
.photo--house{left:0;top:0;width:381px;height:340px;background:linear-gradient(170deg,#b9c6dd 0%,#5f6f93 35%,#3a4a6e 60%,#8c8a92 85%);clip-path:polygon(0 0,46% 0,46% 30%,100% 28%,100% 84%,0 100%)}
.photo--room{left:0;top:0;width:125px;height:135px;background:linear-gradient(150deg,#f4f3f1,#c9ccd0 60%,#8d9096)}
.photo--darkkitchen{left:130px;top:0;width:125px;height:118px;background:linear-gradient(160deg,#3a3a3a,#1e1e1e 60%,#7a6442)}
.photo--greykitchen{left:260px;top:0;width:121px;height:100px;background:linear-gradient(160deg,#4b5560,#2c3238 60%,#6c747c)}
.photo--sink{left:0;top:395px;width:381px;height:135px;background:linear-gradient(100deg,#6b4a2a,#c79a5a 35%,#3c3c3c 70%,#7a7a7a);clip-path:polygon(0 25%,100% 0,100% 100%,0 100%)}

.logo{position:absolute;right:18px;top:20px;display:flex;align-items:center;gap:6px;background:var(--white);padding:8px 10px}
.logo__mark{width:10px;height:10px;background:var(--red)}
.logo__name{font-weight:800;font-size:17px;color:var(--red);letter-spacing:.5px;text-transform:uppercase}

.headline{position:absolute;left:40px;right:20px;top:370px;text-align:center;font-weight:900;line-height:.95;color:var(--black);font-size:30px}
.headline__accent{color:var(--red);font-size:42px}
.web-band__url{position:absolute;right:36px;bottom:16px;color:var(--white);font-weight:700;font-size:14px}

.contact{position:absolute;left:50px;top:288px;color:var(--white)}
.contact__title{font-weight:800;font-size:15px;text-transform:uppercase;margin-bottom:14px}
.contact__people{display:flex;gap:10px;margin-bottom:6px}
.contact__person{font-size:13px;line-height:1.3}
.contact__person + .contact__person{border-left:1px solid var(--white);padding-left:8px}
.contact__person b{display:block;font-weight:700;font-size:12.5px}
.contact__list{list-style:none;font-weight:700;font-size:12px;line-height:1.35}
.contact__list li{display:flex;align-items:flex-start;gap:8px;margin-bottom:4px}
.contact__list svg{flex:none;margin-top:2px}

.about{position:absolute;left:40px;top:150px;width:320px;color:var(--white)}
.about__title{font-weight:800;font-size:19px;margin-bottom:8px}
.about__text{font-size:7px;line-height:1.4;margin-bottom:6px}
.perks{position:absolute;left:40px;top:336px;width:320px}
.perks__title{font-weight:700;font-size:14px;line-height:1.2;color:var(--text-dark);padding-bottom:8px;border-bottom:1.5px solid var(--red);width:265px}
.perks__list{list-style:none;margin-top:14px}
.perks__list li{font-size:8.5px;color:var(--text-dark);margin-bottom:10px;display:flex;gap:8px;align-items:center}
.perks__list li::before{content:"";width:5px;height:5px;border-top:1.5px solid var(--red);border-right:1.5px solid var(--red);transform:rotate(45deg)}

.services{position:absolute;left:30px;top:22px;color:var(--white);width:330px}
.services__title{font-weight:900;font-size:19px}
.services__title span{color:var(--red)}
.services__sub{font-size:10px;margin-top:2px;padding-bottom:10px;border-bottom:1.5px solid var(--white);width:265px}
.services__grid{display:grid;grid-template-columns:1fr 1fr;column-gap:10px;row-gap:12px;margin-top:18px}
.service{display:flex;align-items:center;gap:9px;font-size:10px;line-height:1.15}
.service--wide{grid-column:1 / span 2}
.service__icon{flex:none;width:36px;height:36px}
.corner{position:absolute;right:12px;top:12px}
</style>
</head>
<body>

<!-- Outside spread -->
<section class="spread spread--outside">
  <div class="panel panel--left back-cover">
    <svg class="shapes" viewBox="0 0 381 530" aria-hidden="true">
      <rect width="381" height="530" fill="var(--red)"/>
      <polygon points="0,0 381,0 381,280 120,280 0,150" fill="var(--white)"/>
      <polygon points="0,490 381,470 381,530 0,530" fill="var(--black)"/>
    </svg>
    <div class="photo photo--bath" role="img" aria-label="Bright modern bathroom interior"></div>
    <div class="photo photo--kitchen" role="img" aria-label="White kitchen with bar stools and pendant lights"></div>
    <div class="photo photo--lounge" role="img" aria-label="Living room with downlights and staircase"></div>
    <div class="contact">
      <h2 class="contact__title">Get in contact</h2>
      <div class="contact__people">
        <p class="contact__person">Daniel Reyes<b>☎ 0400 555 190</b></p>
        <p class="contact__person">Marcus Lee<b>☎ 0400 555 190</b></p>
      </div>
      <ul class="contact__list">
        <li><svg width="9" height="9" viewBox="0 0 10 10"><circle cx="5" cy="5" r="4.5" fill="none" stroke="#fff"/><line x1="0.5" y1="5" x2="9.5" y2="5" stroke="#fff"/></svg>www.brightwirecrew.com.au</li>
        <li><svg width="9" height="9" viewBox="0 0 10 10"><rect x="0.5" y="2" width="9" height="6" fill="none" stroke="#fff"/><polyline points="0.5,2 5,6 9.5,2" fill="none" stroke="#fff"/></svg>services@brightwirecrew.com.au</li>
        <li><svg width="9" height="9" viewBox="0 0 10 10"><polyline points="3,1 7,5 3,9" fill="none" stroke="#fff" stroke-width="1.5"/></svg>ABN - 12 345 678 901</li>
        <li><svg width="9" height="11" viewBox="0 0 10 12"><polygon points="6,0 1,7 5,7 3,12 9,4 5,4" fill="#fff"/></svg>Electrical Contractor Licence<br>No.000000X</li>
      </ul>
    </div>
  </div>

  <div class="panel panel--right front-cover">
    <div class="photo photo--house" role="img" aria-label="Two-storey suburban house at dusk with lit windows"></div>
    <svg class="shapes" viewBox="0 0 381 530" aria-hidden="true">
      <polygon points="200,310 381,268 381,290 245,318" fill="var(--red)"/>
      <polygon points="70,470 381,455 381,530 40,530" fill="var(--black)"/>
    </svg>
    <div class="logo"><span class="logo__mark"></span><span class="logo__name">Bright Wire Crew</span></div>
    <h1 class="headline"><span class="headline__accent">24/7</span> SYDNEY<br>ELECTRICIANS</h1>
    <p class="web-band__url">www.brightwirecrew.com.au</p>
  </div>
</section>

<!-- Inside spread -->
<section class="spread spread--inside">
  <div class="panel panel--left about-panel">
    <svg class="shapes" viewBox="0 0 381 530" aria-hidden="true">
      <rect width="381" height="530" fill="var(--white)"/>
      <polygon points="0,140 381,95 381,280 0,310" fill="var(--red)"/>
      <polygon points="0,505 340,505 340,530 0,530" fill="var(--black)"/>
    </svg>
    <div class="photo photo--room" role="img" aria-label="Living room with sofa and chandelier"></div>
    <div class="photo photo--darkkitchen" role="img" aria-label="Dark modern kitchen with under-cabinet lighting"></div>
    <div class="photo photo--greykitchen" role="img" aria-label="Grey kitchen with pendant lights"></div>
    <div class="about">
      <h2 class="about__title">ABOUT US</h2>
      <p class="about__text">Bright Wire Crew is a Sydney-based electrical business specialising in electrical maintenance work for residential, commercial, strata and real estate clients. It began with two mates with a strong desire to change the image of tradies and provide exceptional service. As a team of electricians based in the Inner West of Sydney, we understand the need of everyday people struggling to find good, reliable and trustworthy electricians.</p>
      <p class="about__text">At Bright Wire Crew, we have high expectations of ourselves and strive to improve every day. We're always available around the clock to provide professional advice or give a helping hand when in need.</p>
    </div>
    <div class="perks">
      <h2 class="perks__title">Why the client should sign up with us as a lifetime client</h2>
      <ul class="perks__list">
        <li>Discounted emergency call out fees outside of normal hours</li>
        <li>Lifetime membership price, one time payment</li>
        <li>Exclusive 10% member discount on all future jobs</li>
        <li>Priority on any during business hour jobs or emergencies</li>
      </ul>
    </div>
  </div>

  <div class="panel panel--right services-panel">
    <svg class="shapes" viewBox="0 0 381 530" aria-hidden="true">
      <rect width="381" height="530" fill="var(--black)"/>
    </svg>
    <svg class="corner" width="36" height="70" viewBox="0 0 36 70" aria-hidden="true">
      <polyline points="0,1.5 34.5,1.5 34.5,50" fill="none" stroke="#fff" stroke-width="3"/>
      <line x1="34.5" y1="56" x2="34.5" y2="70" stroke="#fff" stroke-width="3"/>
    </svg>
    <div class="photo photo--sink" role="img" aria-label="Kitchen bench with fresh fruit and a sink"></div>
    <div class="services">
      <h2 class="services__title">OUR <span>SERVICES</span></h2>
      <p class="services__sub">Customer Satisfaction Is Our Highest Priority</p>
      <div class="services__grid">
        <div class="service"><svg class="service__icon" viewBox="0 0 36 36"><circle cx="18" cy="18" r="17" fill="var(--red)" stroke="#fff" stroke-width="2"/><circle cx="18" cy="16" r="5" fill="none" stroke="#fff" stroke-width="1.5"/><line x1="15.5" y1="23" x2="20.5" y2="23" stroke="#fff" stroke-width="1.5"/></svg>Light<br>Installation</div>
        <div class="service"><svg class="service__icon" viewBox="0 0 36 36"><circle cx="18" cy="18" r="17" fill="var(--red)" stroke="#fff" stroke-width="2"/><rect x="11" y="13" width="14" height="10" fill="none" stroke="#fff" stroke-width="1.5"/><line x1="14" y1="18" x2="22" y2="18" stroke="#fff"/></svg>Switchboard<br>Install, Upgrade<br>&amp; Repair</div>
        <div class="service"><svg class="service__icon" viewBox="0 0 36 36"><circle cx="18" cy="18" r="17" fill="var(--red)" stroke="#fff" stroke-width="2"/><rect x="12" y="12" width="12" height="12" rx="2" fill="none" stroke="#fff" stroke-width="1.5"/><line x1="16" y1="16" x2="16" y2="19" stroke="#fff" stroke-width="1.5"/><line x1="20" y1="16" x2="20" y2="19" stroke="#fff" stroke-width="1.5"/></svg>Power Outlets</div>
        <div class="service"><svg class="service__icon" viewBox="0 0 36 36"><circle cx="18" cy="18" r="17" fill="var(--red)" stroke="#fff" stroke-width="2"/><line x1="18" y1="10" x2="18" y2="26" stroke="#fff" stroke-width="1.5"/><line x1="13" y1="14" x2="23" y2="14" stroke="#fff" stroke-width="1.5"/><line x1="14" y1="26" x2="22" y2="26" stroke="#fff" stroke-width="1.5"/></svg>Level 2 ASP</div>
        <div class="service"><svg class="service__icon" viewBox="0 0 36 36"><circle cx="18" cy="18" r="17" fill="var(--red)" stroke="#fff" stroke-width="2"/><polygon points="19,10 13,19 17,19 15,26 23,16 19,16" fill="none" stroke="#fff" stroke-width="1.3"/></svg>Surge<br>Protection</div>
        <div class="service"><svg class="service__icon" viewBox="0 0 36 36"><circle cx="18" cy="18" r="17" fill="var(--red)" stroke="#fff" stroke-width="2"/><rect x="10" y="15" width="16" height="7" rx="2" fill="none" stroke="#fff" stroke-width="1.5"/><circle cx="14" cy="23" r="1.6" fill="#fff"/><circle cx="22" cy="23" r="1.6" fill="#fff"/></svg>EV Electric<br>Vehicle Charging<br>Stations</div>
        <div class="service"><svg class="service__icon" viewBox="0 0 36 36"><circle cx="18" cy="18" r="17" fill="var(--red)" stroke="#fff" stroke-width="2"/><polyline points="12,25 16,19 20,21 24,13" fill="none" stroke="#fff" stroke-width="1.5"/><polyline points="20,13 24,13 24,17" fill="none" stroke="#fff" stroke-width="1.5"/></svg>24/7<br>Emergency<br>Services</div>
        <div class="service"><svg class="service__icon" viewBox="0 0 36 36"><circle cx="18" cy="18" r="17" fill="var(--red)" stroke="#fff" stroke-width="2"/><rect x="11" y="12" width="14" height="5" rx="1" fill="none" stroke="#fff" stroke-width="1.5"/><path d="M14 20 q1 2 0 4 M18 20 q1 2 0 4 M22 20 q1 2 0 4" fill="none" stroke="#fff"/></svg>Smoke Alarms</div>
        <div class="service"><svg class="service__icon" viewBox="0 0 36 36"><circle cx="18" cy="18" r="17" fill="var(--red)" stroke="#fff" stroke-width="2"/><rect x="12" y="10" width="12" height="16" rx="1" fill="none" stroke="#fff" stroke-width="1.5"/><line x1="12" y1="14" x2="24" y2="14" stroke="#fff"/></svg>Electric Hot<br>Water Repairs</div>
        <div class="service"><svg class="service__icon" viewBox="0 0 36 36"><circle cx="18" cy="18" r="17" fill="var(--red)" stroke="#fff" stroke-width="2"/><circle cx="18" cy="18" r="2" fill="#fff"/><circle cx="18" cy="13" r="3" fill="none" stroke="#fff" stroke-width="1.3"/><circle cx="18" cy="23" r="3" fill="none" stroke="#fff" stroke-width="1.3"/><circle cx="13" cy="18" r="3" fill="none" stroke="#fff" stroke-width="1.3"/><circle cx="23" cy="18" r="3" fill="none" stroke="#fff" stroke-width="1.3"/></svg>Ceiling &amp;<br>Exhaust Fans</div>
        <div class="service service--wide"><svg class="service__icon" viewBox="0 0 36 36"><circle cx="18" cy="18" r="17" fill="var(--red)" stroke="#fff" stroke-width="2"/><polyline points="10,18 18,11 26,18" fill="none" stroke="#fff" stroke-width="1.5"/><rect x="12.5" y="17" width="11" height="9" fill="none" stroke="#fff" stroke-width="1.5"/></svg>Real estate, Strata and Commercial</div>
      </div>
    </div>
  </div>
</section>

</body>
</html>
```